WardPivot landing page

The existing website at www.wardpivot-example.com needs updating. I've attached some marketing material for the color scheme to be used and potential content. The tagline should be "Real-Time Operational Intelligence." I want the landing page to be in 3 categories in this order and features within each category. Plenty of images are preferred and wording can be modified.
Wardpivot Command Centre
- Live Incident tracking and reporting with escalation on critical incidents if necessary
- Geofence Monitoring to ensure guards at the right location at the right time.
- Smart scheduling to ensure the correct training and certifications are assigned to the appropriate guard required.
- Camera compatibility to capture live and historical video for incident reporting
WardPivot Back Office Administration
- Automate Police report filing using data from submitted incidents when required.
- Track all required KPIs on a per site basis such as vehicle inspections, patrol tour details, etc
- Payroll and Invoicing using smart shift reports
- Create and manage client sites with configurable geofencing
WardPivot App
- Guard can see all site details and instructions when logging onto shift
- Ability to view all incidents that have occured at that particular site over the last 'x' days. Understand what has been happening and when.
- Report incidents with all relevant information including photo and video
- Recieve alerts when repeat offences are occuring within a configurable vicinity.

Target Market(s)

Retailers and guard companies

Coding

Coded - Design and coding required

Number of Pages Required

1 page

Requirements
Nice to have
• Use the look and feel of the logo in the design

```html
<!DOCTYPE html>
<html lang="en">
<head>
<meta charset="utf-8">
<title>WardPivot — Real-Time Operational Intelligence</title>
<link href="https://fonts.googleapis.com/css2?family=Inter:wght@400;500;600;700;800&display=swap" rel="stylesheet">
<style>
:root{
  --navy:#163356;
  --navy-deep:#0f2745;
  --blue:#2a8ccc;
  --blue-bright:#2b90d6;
  --white:#ffffff;
  --ink:#111111;
  --text:#2b2b2b;
  --soft:#f1f3f6;
  --field-line:#d5dbe3;
}
*{box-sizing:border-box;margin:0;padding:0}
html,body{width:1200px;height:3732px;overflow:hidden}
body{font-family:"Inter",sans-serif;color:var(--text);position:relative;background:var(--white)}
.abs{position:absolute}
.media{position:absolute;display:block}

/* nav */
.nav{left:185px;top:12px;width:832px;height:55px;background:var(--white);display:flex;align-items:center;padding:0 25px;z-index:2}
.brand{display:flex;align-items:center;gap:8px;font-weight:700;font-size:13px;color:var(--blue)}
.brand-dot{width:22px;height:22px;border-radius:50%;background:var(--navy)}
.menu{display:flex;gap:26px;margin-left:132px;font-size:14px;color:#222}
.nav-actions{margin-left:auto;display:flex;gap:10px}
.btn{display:inline-block;background:var(--blue);color:var(--white);font-size:14px;font-weight:500;padding:9px 16px;border-radius:2px}
.btn-outline{display:inline-block;border:1px solid var(--white);color:var(--white);font-size:14px;font-weight:600;padding:9px 16px;border-radius:2px}

/* hero */
.hero{left:0;top:0;width:1200px;height:575px;background:radial-gradient(ellipse at 55% 40%,#3d5670,#1d3552 70%,#142a45)}
.hero-title{top:306px;width:1200px;text-align:center;color:var(--blue-bright);font-size:50px;font-weight:700;line-height:52px;letter-spacing:-1px}
.hero-sub{top:428px;width:1200px;text-align:center;color:var(--white);font-size:14px;line-height:19px}
.hero-cta{top:493px;left:548px}

/* services */
.services{left:0;top:575px;width:1200px;height:664px;background:var(--navy)}
.sec-title{width:1200px;text-align:center;font-size:40px;font-weight:700;letter-spacing:-1px}
.sec-lead{width:1200px;text-align:center;font-size:14px;line-height:18px}
.card{top:758px;width:257px;height:408px;background:var(--white)}
.card .media{left:0;top:0;width:257px;height:189px}
.card h3{position:absolute;left:22px;top:210px;width:215px;font-size:19px;line-height:30px;font-weight:700;color:var(--ink);letter-spacing:-.3px}
.card p{position:absolute;left:22px;width:215px;font-size:13px;line-height:18px;color:#333}
.card .btn{position:absolute;left:22px;top:346px;font-size:13px;padding:9px 16px}

/* features */
.feature-h{font-size:40px;font-weight:700;line-height:40px;letter-spacing:-1px}
.feature-list{width:290px;font-size:13.5px;line-height:18px}
.feature-list p{margin-bottom:18px}
.band{left:0;width:1200px}

/* form */
.field{position:absolute;background:var(--white);border:1px solid var(--field-line);font-size:14px;color:#777;padding:12px 20px}

/* contacts */
.info-card{left:196px;top:3424px;width:326px;height:275px;background:var(--white);padding:30px 32px;font-size:14px;line-height:24px;color:#222}
.info-card h4{font-size:19px;font-weight:600;margin-bottom:6px}
.info-card a{color:var(--blue);text-decoration:none}
</style>
</head>
<body>

<header class="abs nav">
  <div class="brand"><span class="brand-dot"></span>WardPivot</div>
  <nav class="menu"><span>Home</span><span>Features</span><span>Pricing</span><span>Contacts</span></nav>
  <div class="nav-actions"><span class="btn">Request a Demo</span><span class="btn">Log In</span></div>
</header>

<section class="abs hero" role="img" aria-label="Team of operators working together in a dim security control room"></section>
<h1 class="abs hero-title">Real-Time Operational<br>Intelligence.</h1>
<p class="abs hero-sub">Advanced Security Solutions &amp; Workforce Management Protecting People, Assets, and Operations with<br>Real-Time Intelligence. Discover the Future of Security.</p>
<span class="abs hero-cta btn-outline">Learn More</span>

<section class="abs services"></section>
<h2 class="abs sec-title" style="top:606px;color:var(--white)">Our Services</h2>
<p class="abs sec-lead" style="top:673px;color:var(--white)">Hover over pictures to add more cards or rearrange them with the Tools panel.<br>Add multiple cards by selecting multiple images. You can set the number of<br>columns in Block Parameters.</p>

<article class="abs card" style="left:196px">
  <div class="media" role="img" aria-label="Operator monitoring world map screens in a command centre" style="background:linear-gradient(135deg,#1f3a5a,#0d1d33)"></div>
  <h3>Wardpivot<br>Command Centre</h3>
  <span class="btn">Learn more</span>
</article>
<article class="abs card" style="left:472px">
  <div class="media" role="img" aria-label="Staff reviewing data at office workstations" style="background:linear-gradient(135deg,#9aa7b4,#4c5966)"></div>
  <h3>WardPivot Back<br>Office Administration</h3>
  <p style="top:276px">Service Description. You can show/hide the title, subtitle, text, button in the Block Parameters</p>
  <span class="btn">Learn more</span>
</article>
<article class="abs card" style="left:749px">
  <div class="media" role="img" aria-label="Hand holding a phone showing a glowing green security shield" style="background:linear-gradient(135deg,#2f6a55,#0c1a17)"></div>
  <h3>WardPivot App</h3>
  <p style="top:245px">Service Description. You can show/hide the title, subtitle, text, button in the Block Parameters</p>
  <span class="btn">Learn more</span>
</article>

<!-- command centre -->
<h2 class="abs feature-h" style="left:214px;top:1261px;color:var(--ink)">Wardpivot<br>Command<br>Centre</h2>
<div class="abs feature-list" style="left:214px;top:1402px;color:#222">
  <p>Live Incident tracking and reporting with escalation on critical incidents if necessary.</p>
  <p>Geofence Monitoring to ensure guards at the right location at the right time.</p>
  <p>Smart scheduling to ensure the correct training and certifications are assigned to the appropriate guard required.</p>
  <p>Camera compatibility to capture live and historical video for incident reporting</p>
</div>
<div class="media" role="img" aria-label="Engineers discussing work in a control room" style="left:542px;top:1321px;width:465px;height:260px;background:linear-gradient(135deg,#5d6d7c,#26323e)"></div>

<!-- back office -->
<section class="abs band" style="top:1684px;height:434px;background:var(--navy)"></section>
<div class="media" role="img" aria-label="Two colleagues reviewing a tablet in a purple-lit office" style="left:196px;top:1760px;width:465px;height:309px;background:linear-gradient(135deg,#6a4fb0,#2a2048)"></div>
<h2 class="abs feature-h" style="left:700px;top:1744px;color:var(--white)">WardPivot<br>Back Office<br>Administration</h2>
<div class="abs feature-list" style="left:700px;top:1884px;color:var(--white);width:280px">
  <p>Automate Police report filing using data from submitted incidents when required.</p>
  <p>Track all required KPIs on a per site basis such as vehicle inspections, patrol tour details, etc.</p>
  <p>Payroll and Invoicing using smart shift reports.</p>
  <p>Create and manage client sites with configurable geofencing.</p>
</div>

<!-- app -->
<section class="abs band" style="top:2118px;height:429px;background:var(--blue)"></section>
<h2 class="abs feature-h" style="left:214px;top:2176px;color:var(--white)">WardPivot App</h2>
<div class="abs feature-list" style="left:214px;top:2238px;color:var(--white);width:285px">
  <p>Guard can see all site details and instructions when logging onto shift.</p>
  <p>Ability to view all incidents that have occured at that particular site over the last ‘x’ days. Understand what has been happening and when.</p>
  <p>Report incidents with all relevant information including photo and video</p>
  <p>Recieve alerts when repeat offences are occuring within a configurable vicinity.</p>
</div>
<div class="media" role="img" aria-label="Phone displaying a glowing green security shield over code" style="left:542px;top:2207px;width:465px;height:261px;background:linear-gradient(135deg,#2f6a55,#0b1815)"></div>

<!-- cta -->
<section class="abs band" role="img" aria-label="Blue circuit board backdrop" style="top:2547px;height:316px;background:radial-gradient(ellipse at 50% 50%,#264c7c,#152c4c 75%)"></section>
<h2 class="abs sec-title" style="top:2597px;color:var(--white);font-size:50px;line-height:50px">Secure Your<br>Operations Today.</h2>
<p class="abs sec-lead" style="top:2721px;color:var(--white)">Protecting People, Assets, and Operations with Real-Time Intelligence.</p>
<span class="abs btn-outline" style="left:548px;top:2766px">Learn more</span>

<!-- contact form -->
<section class="abs band" style="top:2863px;height:433px;background:var(--blue)"></section>
<h2 class="abs sec-title" style="top:2912px;color:var(--white)">Contact Form</h2>
<p class="abs sec-lead" style="top:2978px;color:var(--white)">To change your notification email, click on any form field below.<br>The number of submissions is limited to 10 per day without the Form Builder.</p>
<div class="field" style="left:333px;top:3045px;width:261px;height:43px">Name</div>
<div class="field" style="left:606px;top:3045px;width:262px;height:43px">Email</div>
<div class="field" style="left:333px;top:3098px;width:535px;height:43px">Phone</div>
<div class="field" style="left:333px;top:3150px;width:535px;height:56px">Message</div>
<p class="abs" style="left:0;top:3232px;width:1188px;text-align:center;color:var(--white);font-size:14px;font-weight:600">Send message</p>

<!-- contacts -->
<section class="abs band" style="top:3296px;height:436px;background:var(--soft)"></section>
<h2 class="abs sec-title" style="top:3350px;color:var(--ink)">Contacts</h2>
<div class="abs info-card">
  <h4>Get in touch</h4>
  <div>Phone: <a href="#">0 (800) 555 01 23</a></div>
  <div><a href="#">www.wardpivot-example.com</a></div>
  <div>email: <a href="#">info@wardpivot-example.com</a></div>
  <div style="margin-top:24px">Address:</div>
  <div>48 Harbor Lane, Newbridge, NY 10099</div>
  <div>Working hours:</div>
  <div>9:00AM - 6:00PM</div>
</div>
<div class="media" role="img" aria-label="Street map showing the office location" style="left:542px;top:3424px;width:465px;height:275px;background:linear-gradient(135deg,#e8ecef,#d3dde6)"></div>

</body>
</html>
```